Plumbing Company After Business Card

Business card for a plumbing business that offers a variety of plumbing services including maintenance, domestic and commercial plumbing. My main focus is to offer high quality professional service. A logo on the card would be ideal. Any other questions feel free to email. Cheers

Looking for something modern and upmarket with preferably a matte black background

Business name is Crestline Plumbing and Gas

Industry/Entity Type

Plumbing

Contact Information for Business Card

Crestline Plumbing and Gas
Marcus Thorvale
0472519306
14 Karrabee Drive, Ascot 3550
crestlineplumbing@mailbay.com.au
ABN 64 915 207 338

Font styles to use
Sans Serif

Colors
1b1b1b
ffffff
3377b5

Requirements
Must have
• Domestic
• Commercial
• Maintenance

```html
<!DOCTYPE html>
<html lang="en">
<head>
<meta charset="utf-8">
<title>Crestline Plumbing and Gas – Business Card</title>
<link rel="stylesheet" href="https://fonts.googleapis.com/css2?family=Source+Sans+3:wght@400;600;700&display=swap">
<style>
  :root {
    --backdrop: #abdff3;
    --card-dark: #222222;
    --card-light: #fbfcfe;
    --ink-light: #ffffff;
    --ink-dark: #222222;
  }
  * { margin: 0; padding: 0; box-sizing: border-box; }
  html, body {
    width: 1200px;
    height: 1000px;
    overflow: hidden;
    background: var(--backdrop);
    font-family: "Source Sans 3", sans-serif;
  }
  .canvas { position: relative; width: 1200px; height: 1000px; }

  .card { position: absolute; }
  .card--front {
    left: 134px; top: 149px; width: 528px; height: 301px;
    background: var(--card-dark);
    color: var(--ink-light);
  }
  .card--back {
    left: 520px; top: 587px; width: 524px; height: 296px;
    background: var(--card-light);
    color: var(--ink-dark);
  }

  .brand-mark { position: absolute; background: currentColor; }

  .front-brand .brand-mark { left: 48px; top: 46px; width: 47px; height: 42px; }
  .front-brand .brand-name {
    position: absolute; left: 104px; top: 47px;
    font-size: 22px; font-weight: 700; letter-spacing: -0.2px; white-space: nowrap;
  }
  .services {
    list-style: none; display: flex; white-space: nowrap;
  }
  .services li::before { content: "•"; margin-right: 4px; }
  .front-brand .services {
    position: absolute; left: 114px; top: 76px;
    font-size: 11px; gap: 10px;
  }

  .holder-name {
    position: absolute; left: 45px; top: 108px;
    font-size: 23px; font-weight: 600; white-space: nowrap;
  }
  .holder-abn {
    position: absolute; left: 46px; top: 139px;
    font-size: 15px; white-space: nowrap;
  }
  .contact {
    position: absolute; right: 32px; top: 207px;
    list-style: none; text-align: right;
    font-size: 15px; line-height: 21px; white-space: nowrap;
  }

  .back-brand .brand-mark { left: 226px; top: 100px; width: 72px; height: 63px; color: var(--ink-dark); }
  .back-brand .brand-name {
    position: absolute; left: 0; right: 0; top: 168px; text-align: center;
    font-size: 34px; font-weight: 700; letter-spacing: -0.3px; white-space: nowrap;
  }
  .back-brand .services {
    position: absolute; left: 0; right: 0; top: 210px;
    justify-content: center; font-size: 17px; gap: 16px;
  }
</style>
</head>
<body>
<main class="canvas">
  <section class="card card--front" aria-label="Card front">
    <div class="front-brand">
      <span class="brand-mark" aria-hidden="true"></span>
      <span class="brand-name">Crestline Plumbing and Gas</span>
      <ul class="services">
        <li>Domestic</li>
        <li>Maintenance</li>
        <li>Commercial</li>
      </ul>
    </div>
    <p class="holder-name">Marcus Thorvale</p>
    <p class="holder-abn">ABN 64 915 207 338</p>
    <ul class="contact">
      <li>0472519306</li>
      <li>14 Karrabee Drive, Ascot 3550</li>
      <li>crestlineplumbing@mailbay.com.au</li>
    </ul>
  </section>

  <section class="card card--back" aria-label="Card back">
    <div class="back-brand">
      <span class="brand-mark" aria-hidden="true"></span>
      <p class="brand-name">Crestline Plumbing and Gas</p>
      <ul class="services">
        <li>Domestic</li>
        <li>Maintenance</li>
        <li>Commercial</li>
      </ul>
    </div>
  </section>
</main>
</body>
</html>
```